Wine Label for a White and a Red Wine from Italy

We have a very good idea of what we want with artwork. We need you to please design a 'template' with the text so we can change out the artwork from year to year. Samples are shown of what we are looking for. We are looking for options with the two basic designs. Brand name of wine is: Valora di Castegno. Both wines are in a light green Bordeaux-style bottle (note: we don't show a light green bottle in the mockup but please remember the bottle is light green). Artwork is provided. We'd like to see either the green or blue butterfly on the white wine, the red butterfly is for the red wine. Please base the design on the attached label from Brailey and/or the attached label from Chateau Mervanges.

Target Market(s)

Millennials, women

Requirements
Must have
• The artwork (butterflies) attached.
Nice to have
• Elegant, readable fonts. Please make the text so it can be changed by the printer. Please make it so the artwork can be changed too.

```html
<!DOCTYPE html>
<html lang="en">
<head>
<meta charset="utf-8">
<title>Valora di Castegno — Barrel Select Labels</title>
<link rel="stylesheet" href="https://fonts.googleapis.com/css2?family=Cormorant+SC:wght@500&family=Cormorant+Garamond:wght@500&family=EB+Garamond:wght@400;500&family=Montserrat:wght@500&display=swap">
<style>
  :root {
    --page: #ffffff;
    --label-paper: #ecebe3;
    --label-edge: #dddcd2;
    --ink-brand: #55524d;
    --ink-text: #3b3833;
    --ink-gold: #6b5418;
    --art-light: #f8d35a;
    --art-deep: #f0aa1c;
  }

  * { margin: 0; padding: 0; box-sizing: border-box; }

  html, body {
    width: 1200px;
    height: 1200px;
    overflow: hidden;
    background: var(--page);
  }

  .label-sheet {
    position: relative;
    width: 1200px;
    height: 1200px;
  }

  .wine-label {
    position: absolute;
    top: 300px;
    width: 440px;
    height: 600px;
    background: var(--label-paper);
    border: 1px solid var(--label-edge);
    text-align: center;
    color: var(--ink-text);
  }

  .wine-label--bianco { left: 120px; }
  .wine-label--rosso  { left: 640px; }

  .brand {
    position: absolute;
    top: 36px;
    left: 0;
    right: 0;
    font-weight: 500;
    color: var(--ink-brand);
    line-height: 1;
  }

  .brand__name {
    display: block;
    font-family: "Cormorant SC", "Times New Roman", serif;
    font-size: 60px;
    letter-spacing: 1px;
  }

  .brand__place {
    display: block;
    margin-top: 2px;
    font-family: "Cormorant Garamond", "Times New Roman", serif;
    font-size: 24px;
    letter-spacing: 1px;
  }

  .cuvee {
    position: absolute;
    top: 160px;
    left: 0;
    right: 0;
    font-family: "EB Garamond", Georgia, serif;
    font-size: 17px;
    letter-spacing: 1px;
    color: var(--ink-gold);
  }

  .artwork {
    position: absolute;
    top: 196px;
    left: 90px;
    width: 260px;
    height: 240px;
    background: linear-gradient(180deg, var(--art-light) 0%, var(--art-deep) 100%);
  }

  .vintage {
    position: absolute;
    top: 456px;
    left: 0;
    right: 0;
    font-family: "EB Garamond", Georgia, serif;
    font-size: 32px;
    line-height: 1;
  }

  .appellation {
    position: absolute;
    top: 498px;
    left: 0;
    right: 0;
    font-family: "EB Garamond", Georgia, serif;
    font-size: 17px;
    line-height: 1.05;
    letter-spacing: 0.5px;
  }

  .producer-note {
    position: absolute;
    top: 552px;
    left: 0;
    right: 0;
    font-family: "Montserrat", Arial, sans-serif;
    font-weight: 500;
    font-size: 10px;
    line-height: 1.35;
  }
</style>
</head>
<body>
<main class="label-sheet">

  <section class="wine-label wine-label--bianco">
    <h1 class="brand">
      <span class="brand__name">Valora</span>
      <span class="brand__place">di Castegno</span>
    </h1>
    <p class="cuvee">BARREL SELECT</p>
    <div class="artwork" role="img" aria-label="Artwork area: painted butterfly for the white wine"></div>
    <p class="vintage">2018</p>
    <p class="appellation">BIANCO<br>PIEMONTE, ITALY</p>
    <p class="producer-note">Artisanly Crafted by Cantina Colle Alto<br>sustainably farmed</p>
  </section>

  <section class="wine-label wine-label--rosso">
    <h1 class="brand">
      <span class="brand__name">Valora</span>
      <span class="brand__place">di Castegno</span>
    </h1>
    <p class="cuvee">BARREL SELECT</p>
    <div class="artwork" role="img" aria-label="Artwork area: painted butterfly for the red wine"></div>
    <p class="vintage">2018</p>
    <p class="appellation">ROSSO<br>PIEMONTE, ITALY</p>
    <p class="producer-note">Artisanly Crafted by Cantina Colle Alto<br>sustainably farmed</p>
  </section>

</main>
</body>
</html>
```